Modern Billboard Ad for Criminal Defense Firm

10.5 x 36 We're looking for something to set us apart from the local competition. Looking for sleek and modern. We're a mid-sized firm in a small market city. We want to give the artist room to be creative on this one.
Thanks

Target Market(s)

Adult clients who have been charged with a crime/DWI

Industry/Entity Type

legal

Font styles to use
Serif
Sans Serif

Requirements
Must have
• Needs to have the firm name in large lettering. Law Offices of Marcus T Whitfield. “PLLC” does not have to be included. Phone number of (555) 384-1927 should be included but not the main focus.
Nice to have
• A call to action or something similar. “Don’t go it alone, call today.”, “ Arrested?”

```html
<!DOCTYPE html>
<html lang="en">
<head>
<meta charset="utf-8">
<title>Law Offices of Marcus T Whitfield – Billboard</title>
<link href="https://fonts.googleapis.com/css2?family=Cinzel:wght@400;500&family=Cormorant+Garamond:wght@500&display=swap" rel="stylesheet">
<style>
  :root{
    --page:#ffffff;
    --board:#ffffff;
    --firm-blue:#0b5199;
    --logo-panel:#eceef1;
    --ink-gray:#555555;
    --photo-light:#a9a9a9;
    --photo-dark:#3f3f3f;
    --badge-dark:#1c2a3a;
    --badge-light:#2fa6e0;
  }
  html,body{margin:0;padding:0;width:1173px;height:1200px;overflow:hidden;background:var(--page);}
  .billboard{
    position:absolute;left:36px;top:439px;width:1100px;height:322px;
    background:var(--board);
    box-shadow:0 18px 40px rgba(0,0,0,.22);
  }
  .name-band{
    position:absolute;left:0;top:26px;width:903px;height:169px;background:var(--firm-blue);
  }
  .logo-panel{
    position:absolute;left:903px;top:26px;width:173px;height:169px;background:var(--logo-panel);
    display:flex;flex-direction:column;align-items:center;justify-content:center;gap:12px;
  }
  .logo-dot{width:38px;height:38px;border-radius:50%;background:var(--firm-blue);}
  .logo-name{
    font-family:"Cinzel",serif;font-weight:400;font-size:13px;letter-spacing:1.5px;color:var(--firm-blue);
    text-align:center;line-height:1.2;
  }
  .attorney-photo{
    position:absolute;left:0;top:-11px;width:247px;height:333px;
    background:linear-gradient(160deg,var(--photo-light) 0%,#7a7a7a 45%,var(--photo-dark) 100%);
    clip-path:polygon(35% 0,62% 0,68% 28%,86% 48%,100% 100%,0 100%,0 44%,28% 30%);
  }
  .firm-name{
    position:absolute;left:215px;width:660px;text-align:center;margin:0;
    font-family:"Cinzel",serif;font-weight:400;color:#fff;white-space:nowrap;line-height:1;
  }
  .firm-name .line-top{position:absolute;left:0;right:0;top:34px;font-size:54px;letter-spacing:4px;}
  .firm-name .line-main{position:absolute;left:0;right:0;top:93px;font-size:60px;letter-spacing:2px;}
  .call-to-action{
    position:absolute;left:280px;top:224px;margin:0;
    font-family:"Cinzel",serif;font-weight:500;font-size:58px;color:var(--ink-gray);line-height:1;
  }
  .phone{
    position:absolute;left:648px;top:238px;
    font-family:"Cormorant Garamond",serif;font-weight:500;font-size:42px;color:var(--ink-gray);line-height:1;
  }
  .award-badge{
    position:absolute;left:964px;top:215px;width:60px;height:84px;
    background:linear-gradient(180deg,var(--badge-light) 0%,var(--badge-dark) 30%,var(--badge-dark) 82%,var(--badge-light) 82%);
  }
</style>
</head>
<body>
  <div class="billboard">
    <div class="name-band"></div>
    <div class="logo-panel">
      <div class="logo-dot"></div>
      <div class="logo-name">Marcus T Whitfield</div>
    </div>
    <div class="attorney-photo" role="img" aria-label="Black and white portrait of the attorney in a vest and tie, jacket over his shoulder"></div>
    <h1 class="firm-name">
      <span class="line-top">Law Offices of</span>
      <span class="line-main">Marcus T Whitfield.</span>
    </h1>
    <p class="call-to-action">Arrested?</p>
    <div class="phone">(555) 384-1927</div>
    <div class="award-badge" role="img" aria-label="Community award winner badge"></div>
  </div>
</body>
</html>
```